Coralbend Pastoral Traders Business Cards

We require business cards revamped with our logo. A few details we would like to use.

1. Round Edges
2. Our logo over the top of a wagyu cattle background photo on one side of the card

Other side of the card has the below details.

1. Person Name (First & Last)
2. Job Position
3. Mobile Number
4. Email Address
5. Website Address

Simple & Neat.

Target Market(s)

Sales

Industry/Entity Type

Agriculture

Contact Information for Business Card

CORALBEND PASTORAL TRADERS

Colors

Designer to choose colors to be used in the design.

Requirements
Must have
• Company Logo

```html
<!DOCTYPE html>
<html lang="en">
<head>
<meta charset="utf-8">
<title>Coralbend Pastoral Traders – Business Cards</title>
<link href="https://fonts.googleapis.com/css2?family=Montserrat:wght@400;500;600;700&display=swap" rel="stylesheet">
<style>
  :root {
    --maroon: #6a1822;
    --maroon-light: #a8434e;
    --paper: #ffffff;
    --ink: #2a2a2a;
    --stage: #3a3b3d;
  }
  * { box-sizing: border-box; margin: 0; padding: 0; }
  html, body {
    width: 1200px; height: 1200px; overflow: hidden;
    background: var(--stage);
    font-family: "Montserrat", sans-serif;
  }
  .sheet {
    width: 1200px; height: 1200px;
    display: flex; flex-direction: column; align-items: center; justify-content: center;
    gap: 60px;
  }
  .card {
    position: relative;
    width: 900px; height: 510px;
    border-radius: 38px;
    overflow: hidden;
  }
  .card--front { background: var(--paper); }
  .card--back { background: var(--maroon); }

  .front-wave { position: absolute; inset: 0; width: 100%; height: 100%; }

  .identity {
    position: absolute; left: 70px; top: 115px;
    color: var(--maroon);
    z-index: 1;
  }
  .identity__name {
    font-size: 50px; font-weight: 700; letter-spacing: 0.5px; line-height: 1;
  }
  .identity__position {
    font-size: 24px; font-weight: 500; color: var(--ink); margin-top: 6px; letter-spacing: 0.5px;
  }
  .contact-list {
    list-style: none; margin-top: 18px; margin-left: 10px;
    color: var(--ink); font-size: 20px; line-height: 1.35;
  }
  .contact-list li { display: flex; align-items: flex-start; gap: 12px; }
  .contact-list svg { width: 20px; height: 20px; flex: none; margin-top: 3px; fill: var(--maroon); }

  .brand {
    position: absolute; display: flex; align-items: center; gap: 16px;
    font-weight: 700; letter-spacing: 1px; line-height: 1.1;
  }
  .brand__dot { flex: none; border-radius: 50%; }
  .brand--front { right: 60px; top: 110px; color: var(--maroon); font-size: 30px; }
  .brand--front .brand__dot { width: 64px; height: 64px; background: var(--maroon); }
  .brand--back {
    left: 50%; top: 50%; transform: translate(-50%, -50%);
    color: var(--paper); font-size: 46px;
  }
  .brand--back .brand__dot { width: 96px; height: 96px; background: var(--paper); }
</style>
</head>
<body>
<main class="sheet">

  <section class="card card--front" aria-label="Business card front">
    <svg class="front-wave" viewBox="0 0 900 510" preserveAspectRatio="none" aria-hidden="true">
      <path fill="var(--maroon-light)" d="M0,510 V478 C180,440 380,430 540,390 C700,345 810,280 900,200 V510 Z"/>
      <path fill="var(--paper)" d="M0,510 V494 C180,456 380,446 540,406 C700,361 810,296 900,216 V510 Z"/>
      <path fill="var(--maroon)" d="M0,510 V502 C180,466 380,456 540,416 C700,371 810,306 900,226 V510 Z"/>
    </svg>

    <div class="brand brand--front">
      <span class="brand__dot"></span>
      <span class="brand__name">CORALBEND<br>PASTORAL TRADERS</span>
    </div>

    <div class="identity">
      <h1 class="identity__name">FULL NAME</h1>
      <p class="identity__position">POSITION</p>
      <ul class="contact-list">
        <li>
          <svg viewBox="0 0 24 24"><path d="M6.6 10.8a15.1 15.1 0 0 0 6.6 6.6l2.2-2.2a1 1 0 0 1 1-.25 11.4 11.4 0 0 0 3.6.57 1 1 0 0 1 1 1V20a1 1 0 0 1-1 1A17 17 0 0 1 3 4a1 1 0 0 1 1-1h3.5a1 1 0 0 1 1 1c0 1.250.2 2.450.57 3.57a1 1 0 0 1-.25 1z"/></svg>
          <span>(000) 000 0000</span>
        </li>
        <li>
          <svg viewBox="0 0 24 24"><path d="M2 5h20v14H2z M4 7v.5l8 5 8-5V7l-8 5z" fill-rule="evenodd"/></svg>
          <span>email@company.com</span>
        </li>
        <li>
          <svg viewBox="0 0 24 24"><path d="M12 2a10 10 0 1 0 0 20 10 10 0 0 0 0-20zm0 2c.9 1.2 1.6 2.9 1.9 5h-3.8c.3-2.1 1-3.8 1.9-5zm-2.3.3A13 13 0 0 0 8.1 9H4.6a8 8 0 0 1 5.1-4.7zm4.6 0A8 8 0 0 1 19.4 9h-3.5a13 13 0 0 0-1.6-4.7zM4.1 11h3.8a17 17 0 0 0 0 2H4.1a8 8 0 0 1 0-2zm5.8 0h4.2a15 15 0 0 1 0 2H9.9a15 15 0 0 1 0-2zm6.2 0h3.8a8 8 0 0 1 0 2h-3.8a17 17 0 0 0 0-2zM4.6 15h3.5c.3 1.8.9 3.4 1.6 4.7A8 8 0 0 1 4.6 15zm5.5 0h3.8c-.3 2.1-1 3.8-1.9 5-.9-1.2-1.6-2.9-1.9-5zm5.8 0h3.5a8 8 0 0 1-5.1 4.7c.7-1.3 1.3-2.9 1.6-4.7z"/></svg>
          <span>www.company.com</span>
        </li>
        <li>
          <svg viewBox="0 0 24 24"><path d="M12 2a7 7 0 0 0-7 7c0 5.3 7 13 7 13s7-7.7 7-13a7 7 0 0 0-7-7zm0 9.5A2.5 2.5 0 1 1 12 6.5a2.5 2.5 0 0 1 0 5z"/></svg>
          <span>123 Name Street, 000<br>Your City, 00000-000</span>
        </li>
      </ul>
    </div>
  </section>

  <section class="card card--back" aria-label="Business card back">
    <div class="brand brand--back">
      <span class="brand__dot"></span>
      <span class="brand__name">CORALBEND<br>PASTORAL TRADERS</span>
    </div>
  </section>

</main>
</body>
</html>
```